New Advertising Company Business Card

A two sided business card. One side with logo only and the other side with my information and maybe my logo again. Looking for something unique and creative, but not too busy. Info would include my name(Marcus Feldon), President, phone number, address, email address, and website. LOGO IS THE BLUE AND WHITE ONE.

Target Market(s)

CEO/VP Level Audience

Industry/Entity Type

Business

Contact Information for Business Card

In Description.

```html
<!DOCTYPE html>
<html lang="en">
<head>
<meta charset="utf-8">
<title>Keystone Media – Business Card</title>
<link href="https://fonts.googleapis.com/css2?family=Montserrat:wght@600;700&family=Open+Sans:wght@400;600&display=swap" rel="stylesheet">
<style>
  :root {
    --bg: #e9e6e1;
    --brand-blue: #1776bf;
    --card-white: #f6f6f6;
    --ink: #2a2a2a;
    --silver: #e4e4e4;
    --shadow: rgba(0, 0, 0, 0.18);
  }
  * { box-sizing: border-box; margin: 0; padding: 0; }
  html, body {
    width: 1200px;
    height: 900px;
    overflow: hidden;
    background: var(--bg);
  }
  .canvas {
    position: relative;
    width: 1200px;
    height: 900px;
    display: flex;
    align-items: center;
    justify-content: center;
    gap: 40px;
  }
  .card {
    position: relative;
    width: 540px;
    height: 309px;
    border-radius: 2px;
    box-shadow: 0 10px 24px var(--shadow);
    overflow: hidden;
  }
  .card--back {
    background: var(--brand-blue);
    display: flex;
    align-items: center;
    justify-content: center;
  }
  .wordmark {
    font-family: "Montserrat", sans-serif;
    font-weight: 700;
    text-transform: uppercase;
    line-height: 1;
    text-align: center;
  }
  .card--back .wordmark {
    color: var(--silver);
    font-size: 40px;
    letter-spacing: 4px;
  }
  .wordmark__sub {
    display: block;
    font-size: 0.52em;
    letter-spacing: 0.42em;
    margin-top: 8px;
  }
  .card--front {
    background: var(--card-white);
    font-family: "Open Sans", sans-serif;
    color: var(--ink);
  }
  .card--front .wordmark {
    position: absolute;
    left: 44px;
    top: 56px;
    text-align: left;
    color: var(--brand-blue);
    font-size: 38px;
    letter-spacing: 3px;
  }
  .person {
    position: absolute;
    left: 44px;
    top: 160px;
  }
  .person__name {
    font-family: "Montserrat", sans-serif;
    font-weight: 700;
    font-size: 17px;
    color: var(--brand-blue);
    text-transform: uppercase;
    letter-spacing: 0.3px;
  }
  .person__role {
    font-size: 13px;
    margin-top: 1px;
  }
  .contact {
    list-style: none;
    margin-top: 10px;
    font-size: 13.5px;
    line-height: 1.6;
  }
  .contact__item {
    display: flex;
    align-items: center;
    gap: 7px;
    white-space: nowrap;
  }
  .contact__icon {
    width: 12px;
    height: 12px;
    fill: var(--brand-blue);
    flex: none;
  }
  .address {
    position: absolute;
    right: 40px;
    top: 165px;
    text-align: right;
    font-size: 11.5px;
    line-height: 1.5;
    font-style: normal;
  }
</style>
</head>
<body>
<main class="canvas">
  <section class="card card--back" aria-label="Card back">
    <div class="wordmark">Keystone<span class="wordmark__sub">Media</span></div>
  </section>

  <section class="card card--front" aria-label="Card front">
    <div class="wordmark">Keystone<span class="wordmark__sub">Media</span></div>

    <div class="person">
      <p class="person__name">Owen Hartley</p>
      <p class="person__role">Creative Director</p>
      <ul class="contact">
        <li class="contact__item">
          <svg class="contact__icon" viewBox="0 0 24 24" aria-hidden="true"><path d="M6.6 10.8a15.1 15.1 0 0 0 6.6 6.6l2.2-2.2a1 1 0 0 1 1-.25 11.4 11.4 0 0 0 3.6.57 1 1 0 0 1 1 1V20a1 1 0 0 1-1 1A17 17 0 0 1 3 4a1 1 0 0 1 1-1h3.5a1 1 0 0 1 1 1c0 1.25.2 2.45.57 3.6a1 1 0 0 1-.25 1z"/></svg>
          (044)987654321
        </li>
        <li class="contact__item">
          <svg class="contact__icon" viewBox="0 0 24 24" aria-hidden="true"><path d="M2 5h20v14H2z"/><path d="M3 6l9 7 9-7" fill="none" stroke="#fff" stroke-width="1.6"/></svg>
          hello@keystonemedia.com
        </li>
        <li class="contact__item">
          <svg class="contact__icon" viewBox="0 0 24 24" aria-hidden="true"><circle cx="12" cy="12" r="10"/><path d="M2 12h20M12 2c3 3 3 17 0 20M12 2c-3 3-3 17 0 20" fill="none" stroke="#fff" stroke-width="1.4"/></svg>
          www.keystonemedia.com
        </li>
      </ul>
    </div>

    <address class="address">
      58, Harbour Lane West,<br>
      Westbrook, 40218
    </address>
  </section>
</main>
</body>
</html>
```